An organic baby/mommy skin care product company needs a web design

We need a web design for an organic baby and mommy skin care product company based in NY/NJ called "Lumo & Pinnet". We have developed a half dozen of all natural, organic baby/mommy skin care products that apply on different part of body. For instance, baby bottom balm/cream/oil to effectively cure/prevent diaper rash etc.

The design is for main/intro page, product page and shipping/packaging page.The theme/template will be uploaded to a CartVeldo 1.4.7.3 enviroment (also looking for alternative solutions).
Updates

Target Market(s)

Young professional parents, educated stay-home moms, caring grandparents.

Industry/Entity Type

Skin Care Product

Requirements
Must have
• Logo on upper left; slideshow pictures (up to 5) on main page;
Nice to have
• Cute background picture (a boy and a girl, etc) font, colors.
Should not have
• Please do not try to list all/most products on the main page. 2 to 3 feature products from each category should be enough.

```html
<!DOCTYPE html>
<html lang="en">
<head>
<meta charset="utf-8">
<title>Lumo &amp; Pinnet — Baby Wash</title>
<link href="https://fonts.googleapis.com/css2?family=Source+Sans+3:wght@400;600;700&family=Chewy&display=swap" rel="stylesheet">
<style>
:root{
  --page-bg:#f6c3d4;
  --page-bg-2:#f9d7e3;
  --white:#ffffff;
  --pink:#e23a79;
  --pink-soft:#fdf0f5;
  --pink-line:#f0c3d3;
  --nav-top:#f9a8c8;
  --nav-bottom:#ee6aa0;
  --text:#3f3f3f;
  --text-dark:#1f1f1f;
  --muted:#8a8a8a;
  --grey-tab:#e6e6e6;
  --olive:#5b5a26;
  --photo-warm:#d9c7a8;
  --photo-bottle:#d9e6d8;
}
*{box-sizing:border-box;margin:0;padding:0}
html,body{width:1200px;height:1195px;overflow:hidden}
body{
  font-family:"Source Sans 3",Arial,sans-serif;
  color:var(--text);
  background:linear-gradient(135deg,var(--page-bg-2),var(--page-bg) 50%,var(--page-bg-2));
  position:relative;
}
.sheet{position:absolute;left:82px;top:22px;width:1032px;height:1152px;background:var(--white);border-radius:4px}
.abs{position:absolute}

/* header */
.top-links{left:668px;top:0;width:347px;height:40px;background:var(--pink-soft);border-radius:0 0 6px 6px;
  font-size:13px;display:flex;align-items:center;justify-content:center;gap:10px;color:var(--text)}
.top-links span.sep{color:var(--muted)}
.brand{left:42px;top:36px;display:flex;align-items:center;gap:12px}
.brand-mark{width:22px;height:22px;border-radius:50%;background:var(--pink)}
.brand-name{font-size:44px;font-weight:700;color:var(--pink);line-height:1}
.slogan{left:212px;top:86px;font-size:18px;color:var(--text)}
.search{left:731px;top:74px;width:274px;height:32px;border:1px solid #e2e2e2;background:#f7f7f7;border-radius:3px;
  font-size:13px;color:var(--muted);padding:7px 12px}
.search svg{position:absolute;right:10px;top:7px}

.main-nav{left:3px;top:126px;width:1011px;height:51px;background:linear-gradient(var(--nav-top),var(--nav-bottom));
  font-family:"Chewy","Source Sans 3",sans-serif;color:var(--white);font-size:17px;letter-spacing:.5px}
.main-nav a{position:absolute;top:14px;color:inherit;text-decoration:none;text-transform:uppercase}

/* product panel */
.product-panel{left:3px;top:181px;width:728px;height:586px;border:1px solid var(--pink-line)}
.panel-head{position:absolute;left:0;top:0;right:0;height:36px;background:#f5f5f5}
.panel-title{position:absolute;left:21px;top:7px;color:var(--pink);font-size:19px}
.sort-label{position:absolute;left:513px;top:10px;font-size:12px;color:var(--text)}
.sort-select{position:absolute;left:569px;top:6px;width:148px;height:24px;border:1px solid var(--pink-line);background:var(--white);
  border-radius:3px;font-size:12px;font-style:italic;color:var(--text);padding:3px 20px}
.sort-select svg{position:absolute;right:10px;top:8px}
.col-divider{position:absolute;left:248px;top:58px;width:1px;height:527px;background:#e3e3e3}

.product-photo{position:absolute;left:42px;top:70px;width:150px;height:158px;border-radius:6px;background:linear-gradient(var(--photo-bottle),#eef3ea)}
.product-name{position:absolute;left:16px;width:217px;top:254px;text-align:center;font-size:18px;color:var(--text-dark)}
.product-blurb{position:absolute;left:16px;width:217px;top:284px;font-size:11.5px;line-height:18px;text-align:justify}
.spec{position:absolute;left:18px;font-size:15.5px;line-height:20px;color:var(--text-dark);white-space:nowrap}
.spec b{font-weight:600;display:inline-block}
.qty-box{position:absolute;left:112px;top:432px;width:57px;height:24px;border:1px solid #ccc;font-size:14px;padding:2px 12px;background:#fafafa}
.cta{position:absolute;left:20px;top:537px;width:214px;height:33px;display:flex;border-radius:4px;overflow:hidden;
  background:linear-gradient(#f78cb8,#ee5b96);color:var(--white);font-size:16px}
.cta span{flex:0 0 auto;display:flex;align-items:center;justify-content:center}
.cta span:first-child{width:88px;border-right:1px solid #f9b2cf}
.cta span:last-child{flex:1}

.tabs{position:absolute;left:269px;top:62px;width:445px;height:41px;border-bottom:1px solid #d8d8d8;display:flex;font-size:15px;color:var(--text-dark)}
.tabs div{padding:12px 23px 0;height:40px}
.tabs .active{background:var(--grey-tab);width:110px;text-align:center;padding:12px 0 0}
.body-copy{position:absolute;font-size:11.5px;line-height:18px;text-align:justify}
.photo-mom{position:absolute;left:558px;top:134px;width:149px;height:193px;background:linear-gradient(160deg,#e7d9be,var(--photo-warm) 60%,#b9c7d0)}
.share-row{position:absolute;left:269px;top:549px;display:flex;gap:6px;font-size:9px}
.share-row span{border:1px solid #c9d3e6;padding:1px 5px;border-radius:2px;color:#3b5b99}
.share-row span.count{border-color:#ccc;color:var(--text)}

/* shopping now */
.cart-box{left:738px;top:181px;width:275px;height:171px;background:var(--pink-soft)}
.cart-head{height:41px;background:linear-gradient(var(--nav-top),var(--nav-bottom));color:var(--white);font-size:19px;padding:8px 20px}
.cart-text{position:absolute;left:22px;top:54px;width:242px;font-size:11.5px;line-height:17px}
.cart-row{position:absolute;left:24px;font-size:11px;font-weight:700;color:var(--olive)}
.cart-row b{position:absolute;left:144px}

.promo{left:740px;width:273px;height:144px;border:1px solid var(--pink-line)}
.promo-title{position:absolute;left:20px;top:16px;font-size:18px;line-height:21px;color:var(--pink)}
.promo-price{position:absolute;left:21px;top:64px;font-size:16px;color:var(--text-dark)}
.promo-price big{font-size:22px}
.promo-btn{position:absolute;left:20px;top:102px;width:87px;height:25px;border-radius:4px;background:linear-gradient(#f78cb8,#ee5b96);
  color:var(--white);font-size:13px;text-align:center;padding-top:3px}
.promo-photo{position:absolute;left:163px;top:22px;width:98px;height:108px;border-radius:6px}

.payments-title{left:767px;top:673px;font-size:18px;color:var(--pink)}
.pay-chip{top:710px;width:30px;height:20px;border:1px solid #ccc;border-radius:2px;background:linear-gradient(#fafafa,#dfdfdf)}

/* featured */
.featured-title{left:15px;top:792px;font-size:19px;color:var(--pink)}
.featured-box{left:18px;top:829px;width:983px;height:225px;border:1px solid var(--pink)}
.featured-photo{position:absolute;left:27px;top:8px;width:115px;height:152px;border-radius:8px;background:linear-gradient(#dfe9df,#f2f5f7)}
.add-cart{position:absolute;left:30px;top:180px;width:122px;height:30px;background:#e7e7e7;font-size:18px;text-align:center;padding-top:2px;color:var(--text)}
.f-name{position:absolute;left:190px;top:18px;font-size:17px;color:var(--pink)}
.f-price{position:absolute;left:190px;top:54px;font-size:17px;color:var(--pink)}
.f-sub{position:absolute;left:191px;top:93px;font-size:13px;font-weight:600;color:var(--olive)}
.f-blurb{position:absolute;left:191px;top:117px;width:172px;font-size:11.5px;line-height:17px;text-align:justify}
.f-divider{position:absolute;left:387px;top:7px;width:1px;height:207px;background:var(--pink)}
.f-copy{position:absolute;left:399px;top:8px;width:556px;font-size:11.5px;line-height:20px;text-align:justify}
.f-more{position:absolute;left:881px;top:187px;font-size:13.5px;color:var(--pink)}

/* footer */
.footer-line{left:18px;top:1067px;width:980px;height:1px;background:#d9d9d9}
.footer-links{left:22px;top:1089px;font-size:12px;color:var(--text-dark);word-spacing:2px}
.copyright{left:22px;top:1119px;font-size:12px;color:var(--text-dark)}
.social{top:1085px;width:22px;height:22px;border-radius:3px;background:linear-gradient(#7fb6e6,#3c7bc4)}
</style>
</head>
<body>
<div class="sheet">
  <nav class="abs top-links">
    <span>Log In</span><span class="sep">|</span><span>Checkout</span><span class="sep">|</span><span>Shopping Cart</span><span class="sep">|</span><span>My Account</span>
  </nav>

  <div class="abs brand">
    <span class="brand-name">Lumo &amp; Pinnet</span>
    <span class="brand-mark"></span>
  </div>
  <div class="abs slogan">slogan goes here</div>

  <div class="abs search">Enter keyword
    <svg width="20" height="18" viewBox="0 0 20 18"><circle cx="7.5" cy="7.5" r="5.5" fill="none" stroke="#bbb" stroke-width="2"/><line x1="11.5" y1="11.5" x2="18" y2="16" stroke="#bbb" stroke-width="2.5" stroke-linecap="round"/></svg>
  </div>

  <nav class="abs main-nav">
    <a style="left:30px">Home</a>
    <a style="left:131px">About us</a>
    <a style="left:254px">Products</a>
    <a style="left:380px">Reviews</a>
    <a style="left:495px">Blog</a>
    <a style="left:588px">Order now</a>
    <a style="left:726px">Testimonials</a>
    <a style="left:877px">Contact</a>
  </nav>

  <section class="abs product-panel">
    <div class="panel-head">
      <div class="panel-title">Buy this Product</div>
      <div class="sort-label">Sort by :</div>
      <div class="sort-select">Category
        <svg width="11" height="7" viewBox="0 0 11 7"><polyline points="1,1 5.5,5.5 10,1" fill="none" stroke="#666" stroke-width="1.5"/></svg>
      </div>
    </div>

    <div class="product-photo" role="img" aria-label="Set of baby wash bottles and pump dispensers"></div>
    <div class="product-name">Molestias Excepturi</div>
    <p class="product-blurb">Neque porro quisquam est, qui dolorem ipsum quia dolor sit amet, consectetur, adipisci velit, sed quia non numquam eius modi tempora incidunt.</p>

    <div class="spec" style="top:369px"><b style="width:76px">Price</b><b style="width:15px">:</b> $ 00.00</div>
    <div class="spec" style="top:401px"><b style="width:76px">Type</b><b style="width:28px">:</b> Baby Wash</div>
    <div class="spec" style="top:433px"><b style="width:76px">Quantity</b><b>:</b></div>
    <div class="qty-box">1</div>
    <div class="spec" style="top:465px"><b style="width:76px">Rating</b><b style="width:18px">:</b>
      <svg width="74" height="16" viewBox="0 0 74 16" style="vertical-align:-2px">
        <g fill="#e876a8" stroke="#b84a80" stroke-width=".6">
          <polygon points="7,1 9,6 14,6 10,9.5 11.5,15 7,11.5 2.5,15 4,9.5 0,6 5,6"/>
          <polygon transform="translate(15 0)" points="7,1 9,6 14,6 10,9.5 11.5,15 7,11.5 2.5,15 4,9.5 0,6 5,6"/>
          <polygon transform="translate(30 0)" points="7,1 9,6 14,6 10,9.5 11.5,15 7,11.5 2.5,15 4,9.5 0,6 5,6"/>
          <polygon transform="translate(45 0)" points="7,1 9,6 14,6 10,9.5 11.5,15 7,11.5 2.5,15 4,9.5 0,6 5,6"/>
        </g>
        <polygon transform="translate(60 0)" fill="#cfcfcf" stroke="#999" stroke-width=".6" points="7,1 9,6 14,6 10,9.5 11.5,15 7,11.5 2.5,15 4,9.5 0,6 5,6"/>
      </svg>
    </div>
    <div class="spec" style="top:497px"><b>Availability :</b>&nbsp; 8</div>

    <div class="cta"><span>Buy Now</span><span>Add to Wishlist</span></div>

    <div class="col-divider"></div>

    <div class="tabs">
      <div class="active">Description</div>
      <div>Ingradients</div>
      <div>How to use</div>
      <div>Reviews</div>
    </div>

    <p class="body-copy" style="left:269px;top:133px;width:276px">Sed ut perspiciatis unde omnis iste natus error sit voluptatem accusantium doloremque laudantium, totam rem aperiam, eaque ipsa quae ab illo inventore veritatis et quasi architecto beatae vitae dicta sunt explicabo. Nemo enim ipsam voluptatem quia voluptas sit aspernatur aut odit aut fugit, sed quia consequuntur magni dolores eos qui ratione voluptatem sequi nesciunt. Neque porro quisquam est, qui dolorem ipsum quia dolor sit amet, consectetur, adipisci velit, sed quia non numquam eius modi tempora incidunt ut labore et dolore magnam aliquam quaerat voluptatem.</p>
    <div class="photo-mom" role="img" aria-label="Mother washing her baby's hands at a kitchen sink"></div>

    <p class="body-copy" style="left:269px;top:353px;width:438px">But I must explain to you how all this mistaken idea of denouncing pleasure and praising pain was born and I will give you a complete account of the system, and expound the actual teachings of the great explorer of the truth, the master-builder of human happiness. No one rejects, dislikes, or avoids pleasure itself, because it is pleasure, but because those who do not know how to pursue pleasure rationally encounter consequences that are extremely painful. Nor again is there anyone who loves or pursues or desires to obtain pain of itself, because it is pain, but because occasionally circumstances occur in which toil and pain can procure him some great pleasure.</p>
    <p class="body-copy" style="left:269px;top:501px;width:438px">At vero eos et accusamus et iusto odio dignissimos ducimus qui blanditiis praesentium voluptatum deleniti atque corrupti quos dolores et quas molestias.</p>

    <div class="share-row">
      <span>Like</span><span class="count">26</span>
      <span style="margin-left:6px">Tweet</span><span class="count">97</span>
      <span style="margin-left:6px;background:#f26a3d;border-color:#f26a3d;color:#fff">Share</span><span class="count">832</span>
    </div>
  </section>

  <aside class="abs cart-box">
    <div class="cart-head">Shopping Now</div>
    <p class="cart-text">None of the other companies has the result we do. So stick to the best that's how you will be the best don't opt for the second best.</p>
    <div class="cart-row" style="top:117px">MY CART<b>0</b></div>
    <div class="cart-row" style="top:139px">TOTAL ITEMS<b>0</b></div>
  </aside>

  <div class="abs promo" style="top:363px">
    <div class="promo-title">Skin Care Product<br>Name here</div>
    <div class="promo-price">Price <big>$19</big></div>
    <div class="promo-btn">learn more</div>
    <div class="promo-photo" role="img" aria-label="Three pump bottles of skin care lotion" style="background:linear-gradient(#eaf3e4,#cfe3c3)"></div>
  </div>
  <div class="abs promo" style="top:514px">
    <div class="promo-title">Skin Care Product<br>Name here</div>
    <div class="promo-price">Price <big>$19</big></div>
    <div class="promo-btn">learn more</div>
    <div class="promo-photo" role="img" aria-label="Cream tube beside its box" style="background:linear-gradient(#f4f6f8,#dfe6ec)"></div>
  </div>

  <div class="abs payments-title">Payments :</div>
  <div class="abs pay-chip" style="left:766px"></div>
  <div class="abs pay-chip" style="left:802px"></div>
  <div class="abs pay-chip" style="left:838px"></div>
  <div class="abs pay-chip" style="left:874px"></div>
  <div class="abs pay-chip" style="left:910px"></div>

  <h2 class="abs featured-title" style="font-weight:400">Featured Products</h2>
  <section class="abs featured-box">
    <div class="featured-photo" role="img" aria-label="Two baby wash bottles with green caps"></div>
    <div class="add-cart">add to cart</div>
    <div class="f-name">Product Name here</div>
    <div class="f-price">Price $25</div>
    <div class="f-sub">Etiam consequat blandit</div>
    <p class="f-blurb">Duis aute irure dolor in reprehenderit in voluptate velit esse cillum dolore eu fugiat nulla pariatur. Excepteur sint occaecat cupidatat non proident.</p>
    <div class="f-divider"></div>
    <div class="f-copy">
      <p>Brightwell Webworks is a web service company, offering a wide range of services which range from designing and development, that is covering almost all the fields in the best possible way. To be the best we know what and how to present beautifully the working of the client's need and their advantages be highlighted. We act in accordance with the Industry certified processes to deliver the best to our clients all over the world.</p>
      <p style="margin-top:10px">The only way to success is through the right path and that's what we provide you. None of the other companies has the result we do. So stick to the best that's how you will be the best don't opt for the second best. Our expertise does not limit itself to web development. Duis aute irure dolor in reprehenderit in voluptate velit esse cillum dolore eu fugiat nulla pariatur. Sed ut perspiciatis unde omnis iste.</p>
    </div>
    <div class="f-more">Learn more</div>
  </section>

  <div class="abs footer-line"></div>
  <nav class="abs footer-links">Home | About Us | Products | Reviews | Blog | Order now | Testimonials | Contact</nav>
  <div class="abs copyright">© 2012 Company Name | All right reserved</div>
  <div class="abs social" style="left:887px"></div>
  <div class="abs social" style="left:911px"></div>
  <div class="abs social" style="left:936px"></div>
  <div class="abs social" style="left:962px"></div>
</div>
</body>
</html>
```